Sleek and elegant promotional banner/sign for The Vellinor Law Firm

We need a design for promotional items like banners, signs, print ads, etc. that includes our firm name - "The Vellinor Law Firm" - and what we do. We advise businesses and individuals on legal matters; we represent individuals and businesses in litigation and transactions; we select and create business entities; we solve legal problems for individuals and businesses, etc. PLEASE DO NOT SIMPLY REPEAT THE PREVIOUS SENTENCE ON THE DESIGN. Please create a tag-line or brief description from ours. We need something that describes what we do in concise and creative manner while communicating trust and confidence. The banner must also include our basic contact information: 948.512-7740 (telephone) and vellinorlaw.com (website). You may use one or more of the attached images, but needn't use any with the right design. The design should be sleek and modern.

Target Market(s)

wealthy individuals and small business owners, entrepreneurs

Industry/Entity Type

Lawyer

Font styles to use
Sans Serif

Colors
33a6d7
0556a4
33b8a4

Requirements
Must have
• Firm name, contact information, BRIEF description of our services, sleek and elegant.
• Also, the design must be horizontal - not vertical.
Nice to have
• I'd like to use one of the images
Should not have
• Cliches

```html
<!DOCTYPE html>
<html lang="en">
<head>
<meta charset="utf-8">
<title>The Vellinor Law Firm — Banner</title>
<link href="https://fonts.googleapis.com/css2?family=Tinos&family=Oswald:wght@500;600&family=Montserrat:wght@600&display=swap" rel="stylesheet">
<style>
  :root {
    --stage: #1c1c1e;
    --white: #ffffff;
    --navy: #0e4486;
    --teal: #33b8a4;
    --ink: #1a1a1a;
    --grey-text: #4a4a4a;
    --stone-light: #d2d2cf;
    --stone-mid: #a6a6a3;
  }
  * { box-sizing: border-box; margin: 0; padding: 0; }
  html, body {
    width: 1200px;
    height: 1000px;
    overflow: hidden;
    background: var(--stage);
  }
  .banner {
    position: absolute;
    left: 50px;
    top: 240px;
    width: 1100px;
    height: 520px;
    overflow: hidden;
    background: var(--white);
  }
  .banner__photo {
    position: absolute;
    left: 0;
    top: 0;
    width: 620px;
    height: 520px;
    background: linear-gradient(160deg, var(--stone-light) 0%, var(--stone-mid) 100%);
  }
  .banner__shapes {
    position: absolute;
    inset: 0;
    width: 1100px;
    height: 520px;
  }
  .firm {
    position: absolute;
    left: 560px;
    top: 28px;
    width: 500px;
  }
  .firm__name {
    display: flex;
    align-items: center;
    gap: 12px;
    font-family: "Tinos", "Times New Roman", serif;
    font-size: 31px;
    line-height: 1;
    color: var(--ink);
    letter-spacing: 0.5px;
    text-transform: uppercase;
  }
  .firm__square {
    width: 26px;
    height: 26px;
    background: var(--ink);
    flex: none;
  }
  .firm__tagline {
    margin-top: 8px;
    padding: 3px 0 2px;
    border-top: 1.5px solid var(--grey-text);
    border-bottom: 1.5px solid var(--grey-text);
    font-family: "Montserrat", Arial, sans-serif;
    font-weight: 600;
    font-size: 12.5px;
    color: var(--grey-text);
    letter-spacing: 0.2px;
    display: inline-block;
    margin-left: 38px;
  }
  .services {
    position: absolute;
    left: 575px;
    top: 140px;
    width: 510px;
    text-align: center;
    font-family: "Oswald", Arial, sans-serif;
    color: var(--white);
  }
  .services__intro {
    font-size: 19px;
    font-weight: 500;
    font-style: italic;
    letter-spacing: 0.3px;
    margin-bottom: 6px;
  }
  .services__row {
    display: flex;
    justify-content: center;
    gap: 26px;
  }
  .service {
    font-size: 35px;
    font-weight: 500;
    line-height: 1.2;
    text-transform: uppercase;
  }
  .service__tick {
    display: inline-block;
    width: 26px;
    height: 22px;
    margin-right: 6px;
    vertical-align: 2px;
  }
  .service--wide { line-height: 1.1; margin-top: 4px; }
  .service--last { margin-top: 10px; }
  .contact {
    position: absolute;
    left: 600px;
    top: 436px;
    width: 500px;
    text-align: center;
    font-family: "Oswald", Arial, sans-serif;
    font-weight: 500;
    color: var(--navy);
  }
  .contact__line {
    font-size: 34px;
    line-height: 48px;
  }
  .contact__phone { color: var(--ink); }
  .contact__web {
    font-family: "Montserrat", Arial, sans-serif;
    font-weight: 600;
    font-size: 16px;
    line-height: 24px;
    letter-spacing: 1px;
    color: var(--grey-text);
  }
</style>
</head>
<body>
  <section class="banner">
    <div class="banner__photo" role="img" aria-label="Photograph of marble courthouse columns on stone steps"></div>

    <svg class="banner__shapes" viewBox="0 0 1100 520" aria-hidden="true">
      <polygon points="500,0 1100,0 1100,520 600,520" fill="var(--white)"/>
      <polygon points="484,0 500,0 600,520 584,520" fill="var(--teal)"/>
      <path d="M522,114 Q800,104 1100,64 L1100,82 Q800,120 525,130 Z" fill="var(--teal)"/>
      <path d="M525,130 Q800,120 1100,82 L1100,425 L582,425 Z" fill="var(--navy)"/>
    </svg>

    <header class="firm">
      <div class="firm__name"><span class="firm__square"></span>The Vellinor Law Firm</div>
      <div class="firm__tagline">PROVIDING EXCEPTIONAL RESULTS FOR ITS CLIENTS</div>
    </header>

    <div class="services">
      <p class="services__intro">EXPERIENCE IN CASES INVOLVING</p>
      <div class="services__row">
        <p class="service"><svg class="service__tick" viewBox="0 0 26 22"><path d="M2 12 L10 19 L24 3" fill="none" stroke="var(--teal)" stroke-width="5"/></svg>Business</p>
        <p class="service"><svg class="service__tick" viewBox="0 0 26 22"><path d="M2 12 L10 19 L24 3" fill="none" stroke="var(--teal)" stroke-width="5"/></svg>Contracts</p>
      </div>
      <p class="service"><svg class="service__tick" viewBox="0 0 26 22"><path d="M2 12 L10 19 L24 3" fill="none" stroke="var(--teal)" stroke-width="5"/></svg>Real Estate</p>
      <p class="service service--wide"><svg class="service__tick" viewBox="0 0 26 22"><path d="M2 12 L10 19 L24 3" fill="none" stroke="var(--teal)" stroke-width="5"/></svg>Shareholder Partnership<br>Disputes</p>
      <p class="service service--last"><svg class="service__tick" viewBox="0 0 26 22"><path d="M2 12 L10 19 L24 3" fill="none" stroke="var(--teal)" stroke-width="5"/></svg>Estate Planning</p>
    </div>

    <div class="contact">
      <p class="contact__line">CONTACT US AT: <span class="contact__phone">948-512-7740</span></p>
      <p class="contact__web">VELLINORLAW.COM</p>
    </div>
  </section>
</body>
</html>
```